1st boys haircut certificate for keepsake

We are blessed to be able to treasure this timeless moment with so many families and the companies that we were getting our certificates from no longer make them so we are looking to make our own professional 1st haircut certificate.
We do service only boys so please keep that in mind. We need a space for the childs name, and date.
Feel free to change the color of the logo as needed. MUST be standard certificate size.

Industry/Entity Type

Barber

Requirements
Must have
• Space for child's name, date and stylist
• Logo or Trimming Nook on it nicely somewhere
• MUST be certificate size that can be printed on card stock paper
Nice to have
• We sometimes call our kids Nook kids....don't know if that helps?
Should not have
• girly things or colors

```html
<!DOCTYPE html>
<html lang="en">
<head>
<meta charset="utf-8">
<title>Trimming Nook Haircuts – 1st Haircut Certificate</title>
<link rel="stylesheet" href="https://fonts.googleapis.com/css2?family=Marcellus&family=Crimson+Text&family=Yesteryear&family=Lobster&display=swap">
<style>
  :root {
    --sky-top: #bcbdc0;
    --sky-light: #e6e7e8;
    --field: #e9eaec;
    --band-white: #f4f4f5;
    --ribbon-red: #be1e2d;
    --ribbon-blue: #27aae1;
    --ink: #231f20;
    --numeral: #3a3a3c;
    --brand: #58595b;
    --rule: #231f20;
  }
  * { margin: 0; padding: 0; box-sizing: border-box; }
  html, body { width: 1200px; height: 848px; overflow: hidden; background: #ffffff; }
  .certificate {
    position: relative;
    width: 1200px;
    height: 848px;
    overflow: hidden;
    font-family: "Crimson Text", Georgia, serif;
    color: var(--ink);
  }
  .certificate__backdrop { position: absolute; inset: 0; }
  .brand {
    position: absolute;
    left: 0; right: 0;
    top: 48px;
    text-align: center;
    font-family: "Marcellus", Georgia, serif;
    font-size: 44px;
    line-height: 1.05;
    letter-spacing: 2px;
    color: var(--brand);
    text-transform: uppercase;
  }
  .ordinal {
    position: absolute;
    left: 512px;
    top: 236px;
    font-family: "Marcellus", Georgia, serif;
    color: var(--numeral);
    white-space: nowrap;
  }
  .ordinal__digit { font-size: 230px; line-height: 1; }
  .ordinal__suffix { font-size: 80px; line-height: 1; margin-left: -8px; }
  .title {
    position: absolute;
    left: 0; right: 0;
    top: 428px;
    text-align: center;
    font-family: "Lobster", "Yesteryear", cursive;
    font-size: 52px;
    color: #000000;
  }
  .field {
    position: absolute;
    display: flex;
    align-items: flex-end;
    white-space: nowrap;
  }
  .field__label { line-height: 1; }
  .field__line {
    display: inline-block;
    border-bottom: 1.5px solid var(--rule);
  }
  .field--recipient { left: 216px; top: 562px; font-size: 25px; }
  .field--recipient .field__line { width: 390px; margin-left: 3px; margin-bottom: 2px; }
  .field--stylist { left: 241px; top: 604px; font-size: 24px; }
  .field--stylist .field__line { width: 207px; margin-left: 32px; margin-bottom: -4px; }
  .field--date { left: 730px; top: 609px; font-size: 18px; }
  .field--date .field__line { width: 148px; margin-left: 12px; margin-bottom: -2px; }
</style>
</head>
<body>
<main class="certificate">
  <svg class="certificate__backdrop" width="1200" height="848" viewBox="0 0 1200 848" aria-hidden="true">
    <defs>
      <radialGradient id="sky" cx="600" cy="300" r="700" gradientUnits="userSpaceOnUse">
        <stop offset="0" stop-color="var(--sky-light)"/>
        <stop offset="0.55" stop-color="#d6d7d9"/>
        <stop offset="1" stop-color="var(--sky-top)"/>
      </radialGradient>
    </defs>
    <rect class="sky" width="1200" height="848" fill="url(#sky)"/>
    <path class="band-white" d="M0,196 Q320,230 545,352 L650,352 Q900,232 1200,202 L1200,848 L0,848 Z" fill="var(--band-white)"/>
    <path class="field-area" d="M0,272 Q320,292 545,372 L690,372 Q950,272 1200,270 L1200,848 L0,848 Z" fill="var(--field)"/>
    <path class="ribbon ribbon--red" d="M0,176 Q320,212 540,345 L540,360 Q310,232 0,198 Z" fill="var(--ribbon-red)"/>
    <path class="ribbon ribbon--red" d="M650,352 Q900,220 1200,182 L1200,204 Q920,238 664,360 Z" fill="var(--ribbon-red)"/>
    <path class="ribbon ribbon--blue" d="M0,236 Q330,258 545,360 L545,377 Q320,292 0,274 Z" fill="var(--ribbon-blue)"/>
    <path class="ribbon ribbon--blue" d="M688,356 Q950,246 1200,236 L1200,270 Q960,274 696,372 Z" fill="var(--ribbon-blue)"/>
  </svg>

  <div class="brand">Trimming Nook<br>Haircuts</div>

  <div class="ordinal"><span class="ordinal__digit">1</span><span class="ordinal__suffix">ST</span></div>

  <h1 class="title">Haircut Certificate</h1>

  <div class="field field--recipient">
    <span class="field__label">This certificate is presented to</span><span class="field__line"></span>
  </div>
  <div class="field field--stylist">
    <span class="field__label">Stylist name</span><span class="field__line"></span>
  </div>
  <div class="field field--date">
    <span class="field__label">Date</span><span class="field__line"></span>
  </div>
</main>
</body>
</html>
```